Brisk Yard, LLC Web Design

I would like a web site design for a new lawn care business I am creating for my son. This is what it looks like now.

http://www.briskyardllc.example

Target Market(s)

Target customer is blue collar or middle class people who do not have time to do all of the grunt work around their home such as mowing the lawn, clearing snow etc. Or they need help moving or moving something such as mulch or wood. Shoot for an economical audience that may not have thought about having these tasks done for them.

Industry/Entity Type

Lawn Care

Colors
acd037
9bcb3c
cadf82
eaf2cf

Requirements
Must have
• I put in greens below. The colors that were available were not the best greens or the greens I would think about. The greens on the web site are more close.
Nice to have
• Will have a few more pictures of the logo guy on different machines. Will upload as soon as I get.

```html
<!DOCTYPE html>
<html lang="en">
<head>
<meta charset="utf-8">
<title>Brisk Yard, LLC</title>
<link rel="stylesheet" href="https://fonts.googleapis.com/css2?family=PT+Sans:wght@400;700&family=PT+Sans+Narrow:wght@400;700&display=swap">
<style>
:root{
  --green-dark:#4f9a1e;
  --green:#6ab42a;
  --green-bright:#8cc63f;
  --green-soft:#acd037;
  --green-pale:#cadf82;
  --tab:#b9dc6a;
  --card-bg:#f2f7ec;
  --card-line:#d9e5cf;
  --text:#6b6b6b;
  --text-dark:#555;
  --footer:#3b3b3b;
  --white:#fff;
}
*{box-sizing:border-box;margin:0;padding:0}
html,body{width:1024px;height:1200px;overflow:hidden;background:var(--white)}
body{position:relative;font-family:"PT Sans",sans-serif;color:var(--text)}
.abs{position:absolute}

/* header */
.top-rule{left:0;top:0;width:1024px;height:5px;background:var(--green)}
.site-header{left:0;top:0;width:1024px;height:101px}
.brand{left:140px;top:30px;display:flex;align-items:center;gap:10px}
.brand-dot{width:30px;height:30px;border-radius:50%;background:var(--green)}
.brand-name{font-family:"PT Sans Narrow",sans-serif;font-weight:700;font-size:30px;color:var(--green-dark)}
.call-tab{left:529px;top:5px;width:341px;height:33px;background:var(--green);border-radius:0 0 3px 3px;color:var(--white);font-family:"PT Sans Narrow",sans-serif;font-size:15px;display:flex;align-items:center;padding-left:14px;gap:8px;letter-spacing:.3px}
.call-tab b,.call-box b,.footer-call b{font-weight:700}
.phone-icon{width:11px;height:17px}
.nav{left:372px;top:74px;display:flex;gap:2px}
.nav a{display:block;width:84px;height:27px;background:var(--tab);color:#5f8a24;font-family:"PT Sans Narrow",sans-serif;font-weight:700;font-size:11px;text-transform:uppercase;text-decoration:none;text-align:center;line-height:29px;border-radius:12px 12px 0 0}
.nav a.active{background:var(--green-bright);color:var(--white)}

/* hero */
.hero{left:0;top:101px;width:1024px;height:299px;background:radial-gradient(ellipse at 40% 45%,#7cc43a 0%,#5fae24 60%,#4a9a18 100%)}
.hero h1{position:absolute;left:139px;top:80px;font-family:"PT Sans Narrow",sans-serif;font-weight:700;font-size:28px;color:var(--white)}
.hero p{position:absolute;left:139px;top:116px;width:360px;font-family:"PT Sans Narrow",sans-serif;font-size:15px;line-height:20px;color:var(--white)}
.call-box{position:absolute;left:140px;top:171px;width:341px;height:32px;background:#3f8a18;color:var(--white);font-family:"PT Sans Narrow",sans-serif;font-size:15px;display:flex;align-items:center;padding-left:12px;gap:8px;letter-spacing:.3px}
.mascot{position:absolute;left:524px;top:0;width:348px;height:299px;background:linear-gradient(180deg,#8fcf4f 0%,#3c7fc0 80%,#c43a2a 100%);opacity:.35;border-radius:120px 120px 0 0}

/* about */
.about-photo{left:136px;top:445px;width:432px;height:150px;border-radius:4px;background:linear-gradient(135deg,#4b4a3e,#9bb84a 45%,#d8f25c 60%,#3c3a34)}
.about h2{position:absolute;left:136px;top:606px;font-family:"PT Sans Narrow",sans-serif;font-weight:400;font-size:24px;color:var(--text-dark)}
.about h2 span{color:var(--green)}
.about p{position:absolute;left:136px;top:643px;width:432px;font-size:12.2px;line-height:17.6px;color:var(--text)}

/* schedule form */
.schedule{left:594px;top:444px;width:296px;height:315px;border:1px solid #d6d6d6;background:var(--white)}
.schedule-head{height:63px;background:linear-gradient(180deg,#7ec23c,#5ba722);display:flex;align-items:center;padding-left:23px;gap:8px;color:var(--white);font-family:"PT Sans Narrow",sans-serif;font-weight:700;font-size:20px;letter-spacing:.3px}
.field{position:absolute;left:23px;width:251px;height:28px;border:1px solid #dcdcdc;font-size:11px;color:#888;padding-left:9px;line-height:26px}
.field .end{position:absolute;right:0;top:0;height:26px;width:29px;border-left:1px solid #dcdcdc}
.submit{position:absolute;left:25px;top:249px;width:86px;height:29px;border:1px solid #bdbdbd;border-radius:15px;background:linear-gradient(#fafafa,#e4e4e4);font-family:"PT Sans Narrow",sans-serif;font-weight:700;font-size:11px;color:#666;text-align:center;line-height:27px}

/* services */
.divider{left:136px;top:786px;width:752px;height:4px;background:repeating-linear-gradient(90deg,#cfcfcf 0 1px,transparent 1px 2px)}
.card{top:894px;width:241px;height:196px;background:var(--card-bg);border:1px solid var(--card-line);border-radius:3px}
.card p{position:absolute;left:14px;top:88px;width:211px;text-align:center;font-family:"PT Sans Narrow",sans-serif;font-size:13px;line-height:17.6px;color:var(--text-dark)}
.btn{position:absolute;left:77px;top:179px;width:88px;height:31px;background:linear-gradient(#76bd3c,#59a525);border:1px solid #4e9220;color:var(--white);font-family:"PT Sans Narrow",sans-serif;font-weight:700;font-size:11px;text-align:center;line-height:29px}
.badge{top:821px;width:144px;height:144px;border-radius:50%;display:flex;align-items:center;justify-content:center;text-align:center;color:var(--white);font-family:"PT Sans Narrow",sans-serif;font-weight:700;font-size:23px;line-height:29px}
.badge.lawn{left:184px;background:radial-gradient(circle at 50% 30%,#6a9c2e,#4c8a1e)}
.badge.snow{left:441px;background:radial-gradient(circle at 40% 35%,#c8443c,#8a8a8a 70%)}
.badge.yard{left:696px;background:radial-gradient(circle at 50% 35%,#c065a0,#5e9a2a 65%)}

/* footer */
.footer{left:0;top:1147px;width:1024px;height:53px;background:var(--footer)}
.social{position:absolute;top:17px;width:26px;height:25px;background:var(--white);border-radius:3px}
.footer-links{position:absolute;left:248px;top:13px;font-size:9px;line-height:18px;color:var(--white)}
.footer-call{position:absolute;right:136px;top:15px;font-family:"PT Sans Narrow",sans-serif;font-size:16px;color:var(--white);letter-spacing:.3px}
</style>
</head>
<body>
<header class="site-header abs">
  <div class="top-rule abs"></div>
  <div class="brand abs"><span class="brand-dot"></span><span class="brand-name">Brisk Yard, LLC</span></div>
  <div class="call-tab abs">
    <svg class="phone-icon" viewBox="0 0 11 17"><rect x=".5" y=".5" width="10" height="16" rx="1.5" fill="none" stroke="#fff"/><rect x="2" y="2.5" width="7" height="5" fill="#fff"/><g fill="#fff"><rect x="2" y="9" width="2" height="1.5"/><rect x="4.5" y="9" width="2" height="1.5"/><rect x="7" y="9" width="2" height="1.5"/><rect x="2" y="12" width="2" height="1.5"/><rect x="4.5" y="12" width="2" height="1.5"/><rect x="7" y="12" width="2" height="1.5"/></g></svg>
    <span>Call Dylan today for a free estimate: <b>920-555-0148</b></span>
  </div>
  <nav class="nav abs">
    <a class="active" href="#">Home</a><a href="#">Lawn Care</a><a href="#">Snow Removal</a><a href="#">Yard Care</a><a href="#">Contact</a><a href="#">Schedule</a>
  </nav>
</header>

<section class="hero abs">
  <h1>With over 10 years of experience,</h1>
  <p>we have been helping people by cutting their lawn, removing snow, cleaning yards or even just moving firewood, mulch or stones.</p>
  <div class="call-box">
    <svg class="phone-icon" viewBox="0 0 11 17"><rect x=".5" y=".5" width="10" height="16" rx="1.5" fill="none" stroke="#fff"/><rect x="2" y="2.5" width="7" height="5" fill="#fff"/><g fill="#fff"><rect x="2" y="9" width="2" height="1.5"/><rect x="4.5" y="9" width="2" height="1.5"/><rect x="7" y="9" width="2" height="1.5"/><rect x="2" y="12" width="2" height="1.5"/><rect x="4.5" y="12" width="2" height="1.5"/><rect x="7" y="12" width="2" height="1.5"/></g></svg>
    <span>Call Dylan today for a free estimate: <b>920-555-0148</b></span>
  </div>
  <div class="mascot" role="img" aria-label="Cartoon mascot in a green cap holding a shovel beside a red lawn mower"></div>
</section>

<div class="about-photo abs" role="img" aria-label="Two crew members in bright yellow shirts next to a green riding mower in a garage"></div>
<section class="about">
  <h2>About <span>Brisk Yard LLC</span></h2>
  <p>Brisk Yard, LLC is the vision of Dylan Marsh, owner and main grunt. For the last 10 years he has been helping people by cutting their lawn, removing snow, cleaning yards or even just moving firewood, mulch or stones.&nbsp; He felt that it was time to take it to the next level and Brisk Yard, LLC was born. Brisk Yard, LLC is a locally owned business headquartered in Green Bay, WI. Dylan takes personal pride in providing cost effective and timely services to his clients.</p>
</section>

<aside class="schedule abs">
  <div class="schedule-head">
    <svg width="16" height="16" viewBox="0 0 16 16"><rect x="1" y="3" width="14" height="12" fill="none" stroke="#d8f0a8" stroke-width="1.5"/><rect x="1" y="3" width="14" height="3" fill="#d8f0a8"/><g fill="#d8f0a8"><rect x="3" y="8" width="2" height="2"/><rect x="7" y="8" width="2" height="2"/><rect x="11" y="8" width="2" height="2"/><rect x="3" y="11" width="2" height="2"/><rect x="7" y="11" width="2" height="2"/></g><rect x="4" y="1" width="1.5" height="3" fill="#d8f0a8"/><rect x="10.5" y="1" width="1.5" height="3" fill="#d8f0a8"/></svg>
    <span>SCHEDULE A SERVICE TODAY</span>
  </div>
  <div class="field" style="top:88px">Lawn Care<span class="end"><svg width="29" height="26"><path d="M11 12h7l-3.5 3.5z" fill="#aaa"/></svg></span></div>
  <div class="field" style="top:123px">Name (required)</div>
  <div class="field" style="top:158px">Phone (required)</div>
  <div class="field" style="top:193px">Date of Appointment (required)<span class="end" style="border:0"><svg width="29" height="26"><rect x="8" y="6" width="14" height="13" fill="none" stroke="#999"/><rect x="8" y="6" width="14" height="3" fill="#999"/><path d="M8 12h14M8 15.5h14M11.5 9v10M15 9v10M18.5 9v10" stroke="#bbb" stroke-width=".8"/></svg></span></div>
  <div class="submit">SUBMIT FORM</div>
</aside>

<div class="divider abs"></div>

<section class="services">
  <article class="card abs" style="left:136px"><p>We are beginning to do commercial properties. and these can be found around Green Bay, Bellevue, DePere, Allouez and Ashwaubenon, in Wisconsin.</p><span class="btn">Read More</span></article>
  <article class="card abs" style="left:392px"><p>We handle everything. We salt, shovel, plow, snowplow your drive way and sidewalks so you have a safe winter and guarantied cleanup</p><span class="btn">Read More</span></article>
  <article class="card abs" style="left:647px"><p>A great way to brighten up your landscape is by adding a fresh layer of mulch. We pride ourselves in helping people with what ever tasks they need done.</p><span class="btn">Read More</span></article>
  <div class="badge lawn abs" role="img" aria-label="Freshly striped lawn with a hedge behind">LAWN CARE</div>
  <div class="badge snow abs" role="img" aria-label="Red pickup truck with a snow plow blade">SNOW<br>REMOVAL</div>
  <div class="badge yard abs" role="img" aria-label="Front yard with flower beds and a porch">YARDCARE</div>
</section>

<footer class="footer abs">
  <span class="social" style="left:133px" aria-label="Social link"></span>
  <span class="social" style="left:171px" aria-label="Social link"></span>
  <span class="social" style="left:209px" aria-label="Social link"></span>
  <div class="footer-links">Sitemap | Privacy Policy<br>Copyright © 2014 - Brisk Yard LLC</div>
  <div class="footer-call">Call Dylan today for a free estimate: <b>920-555-0148</b></div>
</footer>
</body>
</html>
```